Web Design Project

We are looking to for a redesign for www.velpardo.com. Velpardo Systems is a Managed Service Provider of IT solutions based is Calgary, Alberta, Canada. We are currently expanding into the Edmonton market and would like to lauch our new site with our expansion.
The design should be sleak in style and communicate a professional vision to our clients and prospects.

Thanks,
Tomas

Target Market(s)

Small to medium size businesses looking to outsource or complement their IT solutions.

Industry/Entity Type

It Professional

```html
<!DOCTYPE html>
<html lang="en">
<head>
<meta charset="utf-8">
<title>Velpardo Systems | Managed IT Service Professionals</title>
<link rel="stylesheet" href="https://fonts.googleapis.com/css2?family=Source+Sans+3:wght@400;600&display=swap">
<style>
  :root {
    --paper: #e4e1dd;
    --paper-light: #eeebe8;
    --panel: #212121;
    --fold: #4d4d4d;
    --red: #e1282d;
    --ink: #231f20;
    --white: #ffffff;
  }
  * { box-sizing: border-box; margin: 0; padding: 0; }
  html, body { width: 1200px; height: 708px; overflow: hidden; }
  body {
    position: relative;
    font-family: "Source Sans 3", "Myriad Pro", sans-serif;
    background: radial-gradient(ellipse at 40% 30%, var(--paper-light), var(--paper) 70%);
    color: var(--white);
  }
  .brand {
    position: absolute; right: 100px; top: 36px;
    font-size: 40px; font-weight: 400; line-height: 48px;
    color: var(--ink); white-space: nowrap;
  }
  .site-nav { position: absolute; left: 58px; top: 84px; width: 740px; height: 43px; }
  .site-nav svg { position: absolute; inset: 0; }
  .nav-link {
    position: absolute; top: 4px; font-size: 26px; line-height: 36px;
    color: var(--white); text-decoration: none; white-space: nowrap;
  }
  .nav-link.is-current { font-size: 29px; }
  .hero {
    position: absolute; left: 59px; top: 126px; width: 1079px; height: 311px;
    background: var(--panel);
    clip-path: polygon(0 0, calc(100% - 26px) 0, 100% 26px, 100% 100%, 0 100%);
  }
  .hero::after, .card::after {
    content: ""; position: absolute; top: 0; right: 0;
    width: 26px; height: 26px;
    background: linear-gradient(45deg, var(--fold) 50%, transparent 50%);
  }
  .hero-title {
    position: absolute; left: 34px; top: 70px;
    font-size: 31px; font-weight: 400; line-height: 36px;
  }
  .hero-text {
    position: absolute; left: 34px; top: 134px; width: 490px;
    font-size: 15.5px; line-height: 20px; white-space: nowrap;
  }
  .hero-photo {
    position: absolute; left: 519px; top: 39px; width: 520px; height: 232px;
    background: #050505; padding: 7px 11px 8px 9px;
  }
  .hero-photo-fill {
    width: 100%; height: 100%;
    background: linear-gradient(180deg, #f4f4f4, #ffffff 60%, #e8e8e8);
  }
  .card {
    position: absolute; top: 451px; height: 199px;
    background: var(--panel);
    border-top: 10px solid var(--red);
    clip-path: polygon(0 0, calc(100% - 22px) 0, 100% 22px, 100% 100%, 0 100%);
  }
  .card::after { width: 22px; height: 22px; }
  .card-title {
    position: absolute; left: 13px; top: 13px;
    font-size: 26px; font-weight: 400; line-height: 30px;
  }
  .card-text {
    position: absolute; left: 26px; top: 46px;
    font-size: 19px; line-height: 24px;
  }
  .card-media {
    position: absolute; top: 36px; width: 141px; height: 105px;
    border: 3px solid var(--red);
  }
  .card-spotlight { left: 59px; width: 335px; }
  .card-spotlight .card-media { left: 184px; background: linear-gradient(135deg, #0d2233, #1f5f80 55%, #7a1d22); }
  .card-partners { left: 429px; width: 336px; }
  .card-partners .card-title { left: 14px; }
  .card-partners .card-text { left: 25px; }
  .card-partners .card-media { left: 180px; background: var(--panel); display: flex; align-items: center; justify-content: center; }
  .partner-badge { width: 84px; height: 40px; background: #4a4a4a; }
  .card-support { left: 802px; width: 336px; }
  .card-support .card-title { left: 18px; }
  .card-support .card-text { left: 31px; }
  .card-support .card-media { left: 181px; background: linear-gradient(135deg, #cfd6dc, #d9a584 55%, #7a4a30); }
</style>
</head>
<body>
  <header class="brand">Velpardo Systems</header>

  <nav class="site-nav" aria-label="Main">
    <svg width="740" height="43" viewBox="0 0 740 43" aria-hidden="true">
      <path fill="#e1282d" d="M547 43 V14 Q547 2 560 2 H700 Q712 2 720 16 L734 43 Z"/>
      <path fill="#e1282d" d="M408 43 V14 Q408 2 421 2 H525 Q537 2 545 16 L559 43 Z"/>
      <path fill="#e1282d" d="M265 43 V14 Q265 2 278 2 H385 Q397 2 405 16 L419 43 Z"/>
      <path fill="#e1282d" d="M125 43 V14 Q125 2 138 2 H243 Q255 2 263 16 L277 43 Z"/>
      <path fill="#212121" d="M0 43 V14 Q0 1 13 1 H103 Q115 1 123 15 L138 43 Z"/>
    </svg>
    <a class="nav-link is-current" href="#" style="left:17px">Home</a>
    <a class="nav-link" href="#" style="left:142px">About Us</a>
    <a class="nav-link" href="#" style="left:285px">Solutions</a>
    <a class="nav-link" href="#" style="left:434px">Services</a>
    <a class="nav-link" href="#" style="left:566px">Contact Us</a>
  </nav>

  <section class="hero">
    <h1 class="hero-title">Managed IT Service Professionals</h1>
    <p class="hero-text">Velpardo Systems employs an innovative managed service solution to<br>provide our clients with technical expertise and superb customer<br>service. Our goal is to ensure that our clients business requirements<br>align with their technical needs in order to maximize their benefits</p>
    <div class="hero-photo">
      <div class="hero-photo-fill" role="img" aria-label="Photo of a row of server towers with a businessman leaning on them"></div>
    </div>
  </section>

  <section class="card card-spotlight">
    <h2 class="card-title">Spotlight</h2>
    <p class="card-text">Keep your data<br>secure and readily<br>available with our<br>online backup<br>service</p>
    <div class="card-media" role="img" aria-label="Image of glowing padlocks over digital data"></div>
  </section>

  <section class="card card-partners">
    <h2 class="card-title">Partners</h2>
    <p class="card-text">We work with the<br>best to bring you<br>the best.</p>
    <div class="card-media" aria-label="Partner badge"><span class="partner-badge"></span></div>
  </section>

  <section class="card card-support">
    <h2 class="card-title">Live Support</h2>
    <p class="card-text">Click here to<br>access our Live<br>support</p>
    <div class="card-media" role="img" aria-label="Photo of a support agent with a headset"></div>
  </section>
</body>
</html>
```